RJ Penhall & Associates

Create a website encompassing design work already carried out for business card.
Small accounting practice, business accounting and management, superannuation, audit, taxation.

```html
<!DOCTYPE html>
<html lang="en">
<head>
<meta charset="utf-8">
<title>RJ Penhall &amp; Associates</title>
<link rel="stylesheet" href="https://fonts.googleapis.com/css2?family=Open+Sans:wght@400;600;700&display=swap">
<style>
:root{
  --navy:#1d3a66;
  --blue:#3b8fd8;
  --blue-light:#a8cdee;
  --blue-pale:#dcebf8;
  --text:#555b63;
  --muted:#8a9098;
  --white:#ffffff;
  --footer:#1c3b63;
  --rule:#d9dee4;
}
*{box-sizing:border-box;margin:0;padding:0}
html,body{width:822px;height:1200px;overflow:hidden}
body{font-family:"Open Sans",Arial,sans-serif;color:var(--text);background:var(--white);font-size:9px;line-height:1.45}
a{color:inherit;text-decoration:none}

.site-header{height:74px;display:flex;align-items:center;justify-content:space-between;padding:0 34px 0 40px;background:var(--white)}
.brand{display:flex;align-items:center;gap:10px;color:var(--navy);font-weight:700;font-size:19px;line-height:1.05}
.brand-mark{width:30px;height:30px;background:var(--navy)}
.main-nav{display:flex;gap:2px}
.main-nav a{font-size:9.5px;font-weight:600;color:var(--navy);padding:8px 11px}
.main-nav a.active{background:var(--blue);color:var(--white)}

.service-band{height:30px;background:var(--blue);color:var(--white);font-weight:600;font-size:10.5px;display:flex;align-items:center;padding-left:40px}

.hero{height:282px;background:linear-gradient(160deg,#f4f6f8 0%,#cfd5db 45%,#8d96a0 100%)}

.welcome{padding:24px 70px 22px;text-align:center}
.welcome h1{font-size:20px;font-weight:600;color:#333;margin-bottom:10px}
.welcome h1 span{color:var(--blue)}
.welcome p{font-size:8.5px;color:var(--muted)}

.benefits{background:var(--blue-light);padding:18px 40px 20px;height:372px}
.benefits h2{color:var(--white);font-size:17px;font-weight:600;margin-bottom:16px}
.benefit-grid{display:grid;grid-template-columns:repeat(4,1fr);gap:14px}
.benefit-photo{height:138px;background:linear-gradient(150deg,#e9eef3,#9fb0c2)}
.benefit-card h3{color:var(--navy);font-size:10.5px;font-weight:700;margin:12px 0 6px;line-height:1.2;min-height:25px}
.benefit-card p{color:var(--white);font-size:8.3px;margin-bottom:6px}
.read-more{color:var(--navy);font-weight:700;font-size:8.5px}

.info{display:grid;grid-template-columns:1.15fr 1fr 1fr;gap:30px;padding:20px 40px 0;height:252px}
.info h4{font-size:12px;font-weight:600;color:#333;margin-bottom:12px}
.news-item{display:flex;gap:10px;margin-bottom:14px}
.news-date{width:30px;text-align:center;border:1px solid var(--rule)}
.news-date b{display:block;font-size:14px;color:#333}
.news-date small{font-size:7.5px;color:var(--muted)}
.news-item h5{font-size:9.5px;color:#333;font-weight:600}
.news-item .meta{color:var(--muted);font-size:7.5px}
.news-item p{font-size:8px}
.news-item p a{color:var(--blue)}
.about-list{list-style:none}
.about-list li{border:1px solid var(--rule);padding:5px 8px;margin-bottom:6px;font-size:8px;color:#444;display:flex;justify-content:space-between}
.about-list li.open{background:var(--blue-pale)}
.about-text{font-size:8px;margin:2px 0 8px}
.quote{background:#f2f4f6;padding:10px 12px;font-size:8px;position:relative}
.author{display:flex;align-items:center;gap:8px;margin-top:14px;justify-content:flex-end}
.author-photo{width:32px;height:32px;background:#b9c3cd}
.author b{display:block;color:#333;font-size:9px}
.author small{color:var(--muted);font-size:7.5px}

.site-footer{background:var(--footer);color:var(--white);height:58px;padding:12px 40px;display:flex;justify-content:space-between;align-items:flex-start;font-size:8.5px}
.site-footer nav{margin-bottom:5px}
.site-footer p{color:#c2d0e0;font-size:8px}
.social{display:flex;gap:5px}
.social span{width:17px;height:17px;background:#3e6da0;display:block}
.social span.hl{background:#d9533f}
</style>
</head>
<body>
<header class="site-header">
  <a class="brand" href="#"><span class="brand-mark"></span><span>RJ Penhall<br>&amp; Associates.</span></a>
  <nav class="main-nav">
    <a class="active" href="#">Home</a><a href="#">About Us</a><a href="#">Services</a><a href="#">Projects</a><a href="#">Careers</a><a href="#">Blog</a><a href="#">Contact Us</a>
  </nav>
</header>
<div class="service-band">Accountant · Business Solutions · Management · Superannuation · Audit</div>
<section class="hero" role="img" aria-label="Desktop calculator resting on financial charts and reports"></section>

<section class="welcome">
  <h1>Welcome To <span>RJ Penhall &amp; Associates</span></h1>
  <p>We help small businesses and families keep their finances clear, compliant and ready for growth. Our team offers practical advice on business accounting, tax planning, superannuation and audit, with the personal care of a local practice. Talk to us about a plan that suits your goals and we will guide you through every step with straightforward support.</p>
</section>

<section class="benefits">
  <h2>Benfits Of Business</h2>
  <div class="benefit-grid">
    <article class="benefit-card">
      <div class="benefit-photo" role="img" aria-label="Team meeting around a desk"></div>
      <h3>Business Accounting &amp; Management</h3>
      <p>Clear monthly accounts, cash flow reporting and budgets that help you run the business with confidence.</p>
      <a class="read-more" href="#">Read More...</a>
    </article>
    <article class="benefit-card">
      <div class="benefit-photo" role="img" aria-label="Hands reviewing financial papers"></div>
      <h3>Superannuation</h3>
      <p>Setup and ongoing care for self managed funds, with annual returns and sound retirement planning.</p>
      <a class="read-more" href="#">Read More...</a>
    </article>
    <article class="benefit-card">
      <div class="benefit-photo" role="img" aria-label="Pen and calculator on printed charts"></div>
      <h3>Audit</h3>
      <p>Independent audits carried out with care, giving owners and members trust in every reported figure.</p>
      <a class="read-more" href="#">Read More...</a>
    </article>
    <article class="benefit-card">
      <div class="benefit-photo" role="img" aria-label="Bar charts and graphs on a desk"></div>
      <h3>Taxation</h3>
      <p>Personal and company tax returns, lodgement planning and advice to keep your obligations on track.</p>
      <a class="read-more" href="#">Read More...</a>
    </article>
  </div>
</section>

<section class="info">
  <div>
    <h4>Latest News</h4>
    <div class="news-item">
      <div class="news-date"><b>21</b><small>Mar</small></div>
      <div><h5>This is a Standard Post</h5><div class="meta">3 Comments</div>
      <p>New tax changes for small firms this year and what they mean for your next return. <a href="#">Read more</a></p></div>
    </div>
    <div class="news-item">
      <div class="news-date"><b>19</b><small>Mar</small></div>
      <div><h5>This is a Standard Post</h5><div class="meta">2 Comments</div>
      <p>Simple steps to review your super fund before the end of the financial year. <a href="#">Read more</a></p></div>
    </div>
  </div>
  <div>
    <h4>More about us</h4>
    <ul class="about-list">
      <li>Our Mission<span>+</span></li>
      <li class="open">Our Values<span>−</span></li>
    </ul>
    <p class="about-text">We believe in honest advice, plain language and lasting relationships with every client we serve in our community.</p>
    <ul class="about-list"><li>Our Team<span>+</span></li></ul>
  </div>
  <div>
    <h4>Testimonials</h4>
    <div class="quote">Their team made our yearly accounts simple and stress free. Friendly, prompt and always ready to help.</div>
    <div class="author">
      <div><b>Daniel Marsh</b><small>Business Owner</small></div>
      <div class="author-photo" role="img" aria-label="Client portrait"></div>
    </div>
  </div>
</section>

<footer class="site-footer">
  <div>
    <nav>Home | About | Practices | People | Events | Contact | Site Map | Privacy Policy</nav>
    <p>Copyright © 2014 RJ Penhall &amp; Associates. All Rights Reserved</p>
  </div>
  <div class="social"><span></span><span></span><span class="hl"></span><span></span><span></span></div>
</footer>
</body>
</html>
```